The Brightwater Compass Business Card

We need an attractive business card with the logo that we bought from ArtVantly last year.
Our mission is to contribute to change the way today's leaders manage business companies bringing value to the workplace and helping them to build a new model of creating wealth.
Our logo is clear about our values : we seek Positive Change through People and are convinced that the pursuit of individual well-being and the chase of economic results can converge with the right management.
Management Consulting
Corinne Fabrelle
+34 612 98 70 31
corinne.fabrelle@thebrightwatercompass-mail.net
www.thebrightwatercompass-mail.net

```html
<!DOCTYPE html>
<html lang="en">
<head>
<meta charset="utf-8">
<title>The Brightwater Compass – Business Card</title>
<link rel="stylesheet" href="https://fonts.googleapis.com/css2?family=Montserrat:wght@400;600;700&display=swap">
<style>
  :root {
    --page-bg: #f5f5f5;
    --card-teal: #108482;
    --brand-faint: #3e9794;
    --brand-teal: #17807d;
    --name-green: #16a58d;
    --body-text: #3d3d3d;
    --card-white: #ffffff;
    --card-shadow: 0 6px 10px rgba(0, 0, 0, 0.18);
  }
  * { margin: 0; padding: 0; box-sizing: border-box; }
  html, body {
    width: 1200px;
    height: 1200px;
    overflow: hidden;
    background: var(--page-bg);
    font-family: "Montserrat", sans-serif;
  }
  .canvas { position: relative; width: 1200px; height: 1200px; }

  .card {
    position: absolute;
    left: 262px;
    width: 676px;
    height: 386px;
    box-shadow: var(--card-shadow);
  }
  .card--front { top: 185px; background: var(--card-teal); }
  .card--back  { top: 629px; background: var(--card-white); }

  .brand {
    position: absolute;
    display: flex;
    flex-direction: column;
    align-items: center;
  }
  .brand__dot { border-radius: 50%; }
  .brand__name {
    font-weight: 600;
    white-space: nowrap;
    letter-spacing: 0.02em;
  }

  .card--front .brand {
    left: 0; right: 0; top: 118px;
  }
  .card--front .brand__dot {
    width: 70px; height: 70px;
    background: var(--brand-faint);
    margin-bottom: 28px;
  }
  .card--front .brand__name {
    font-size: 30px;
    color: var(--brand-faint);
  }

  .card--back .brand {
    left: 400px; width: 244px; top: 54px;
  }
  .card--back .brand__dot {
    width: 44px; height: 44px;
    background: var(--brand-teal);
    margin-bottom: 14px;
  }
  .card--back .brand__name {
    font-size: 15px;
    color: var(--brand-teal);
  }

  .contact {
    position: absolute;
    left: 55px;
    top: 243px;
  }
  .contact__name {
    font-size: 22px;
    font-weight: 700;
    color: var(--name-green);
    margin-bottom: 6px;
  }
  .contact__line {
    font-size: 16px;
    font-weight: 400;
    color: var(--body-text);
    line-height: 21.6px;
  }
</style>
</head>
<body>
  <main class="canvas">
    <section class="card card--front" aria-label="Card front">
      <div class="brand">
        <div class="brand__dot"></div>
        <div class="brand__name">The Brightwater Compass</div>
      </div>
    </section>

    <section class="card card--back" aria-label="Card back">
      <div class="brand">
        <div class="brand__dot"></div>
        <div class="brand__name">The Brightwater Compass</div>
      </div>
      <div class="contact">
        <p class="contact__name">Corinne Fabrelle</p>
        <p class="contact__line">+34 612 98 70 31</p>
        <p class="contact__line">corinne.fabrelle@thebrightwatercompass-mail.net</p>
        <p class="contact__line">www.thebrightwatercompass-mail.net</p>
      </div>
    </section>
  </main>
</body>
</html>
```